Stationary and business cards for Meridale Wellness Clinic
Brightwater Meridale Wellness Clinic
Stationary and business cards for Meridale Wellness Clinic - Health
Creative Brief
Use same font as used in my logo
Use whatever fonts you feel works with the logo
Bright & Fun-filled
Dr. Marcus T. Falk
Chiropractic Physician
5182 Orvalle Park Rd. Ste. B Sarasota, FL 34871
wellpath7crew@mailnest.example
www.falkspinecare.example
when they go to the website, they need to click on other services in the top right of the page, and go to: functional endocrine, to read about what I do . I'm not sure how we can direct them to do that on a business card. Also, this is a separate business located within Falk Chiropractic Center,and has nothing to do with Chiropractic Care...... Use whatever fonts you feel works with the logo, or the same as the logo
Lack of energy, sleep problems, weight gain, and body pains are not normal processes of aging...You don't have to live with it! Call us today to reserve a seat at our next free seminar to learn how we can help you!

```html
<!DOCTYPE html>
<html lang="en">
<head>
<meta charset="utf-8">
<title>Meridale Wellness Clinic – Business Cards</title>
<link rel="stylesheet" href="https://fonts.googleapis.com/css2?family=PT+Serif:wght@400;700&display=swap">
<style>
  :root {
    --backdrop: #4a4a4c;
    --card: #ffffff;
    --green: #5aa51e;
    --green-dark: #3e7f14;
    --green-light: #8cc63f;
    --orange: #e8731a;
    --ink: #4d4d4d;
    --rule: #c9c9c9;
  }
  * { box-sizing: border-box; margin: 0; padding: 0; }
  html, body { width: 1200px; height: 852px; overflow: hidden; }
  body {
    background: var(--backdrop);
    font-family: "PT Serif", Georgia, serif;
    color: var(--ink);
    position: relative;
  }
  .card {
    position: absolute;
    width: 620px;
    height: 354px;
    background: var(--card);
    border-radius: 22px;
    overflow: hidden;
    box-shadow: 0 10px 24px rgba(0,0,0,.35);
  }
  .card--front { left: 60px; top: 64px; }
  .card--back { left: 520px; top: 434px; }
  .card__band {
    position: absolute; left: 0; top: 0; bottom: 0; width: 30px;
    background: linear-gradient(90deg, var(--green-dark), var(--green) 55%, var(--green-light));
  }
  .card__stripe {
    position: absolute; left: 30px; top: 0; bottom: 0; width: 4px;
    background: var(--orange);
  }
  .brand { position: absolute; display: flex; align-items: center; gap: 12px; }
  .brand__dot {
    width: 54px; height: 54px; border-radius: 50%;
    background: var(--green); flex: none;
  }
  .brand__name { color: var(--green); font-weight: 400; line-height: 1.05; }
  .brand__name .line1 { display: block; font-size: 34px; letter-spacing: .5px; }
  .brand__name .line2 { display: block; font-size: 15px; letter-spacing: 1px; margin-top: 2px; }
  .identity { position: absolute; }
  .identity__name { color: var(--green); font-weight: 700; font-size: 17px; }
  .identity__title { color: var(--orange); font-weight: 700; font-size: 13px; margin: 6px 0 8px; }
  .identity__address { font-size: 13px; line-height: 1.5; }
  .divider { position: absolute; width: 1px; background: var(--rule); }
  .contacts { position: absolute; list-style: none; font-size: 12.5px; }
  .contacts li { display: flex; align-items: center; gap: 8px; height: 20px; }
  .contacts svg { width: 13px; height: 13px; flex: none; fill: var(--green); }
</style>
</head>
<body>

<svg width="0" height="0" style="position:absolute" aria-hidden="true">
  <symbol id="icon-phone" viewBox="0 0 16 16"><path d="M3.5 1.5l2.5 0 1 3.5-1.8 1.2a8 8 0 0 0 4.6 4.6L11 9l3.5 1v2.5A1.8 1.8 0 0 1 12.7 14 11 11 0 0 1 2 3.3 1.8 1.8 0 0 1 3.5 1.5z"/></symbol>
  <symbol id="icon-fax" viewBox="0 0 16 16"><rect x="4" y="1.5" width="8" height="4"/><rect x="1.5" y="6" width="13" height="6" rx="1.2"/><rect x="4" y="10" width="8" height="4.5" fill="#fff" stroke="currentColor"/></symbol>
  <symbol id="icon-mail" viewBox="0 0 16 16"><path d="M1.5 3.5h13v9h-13z M1.5 3.5L8 9l6.5-5.5" /></symbol>
  <symbol id="icon-web" viewBox="0 0 16 16"><circle cx="8" cy="8" r="6.5"/><path d="M1.5 8h13M8 1.5c-3 3.5-3 9.5 0 13M8 1.5c3 3.5 3 9.5 0 13" stroke="#fff" stroke-width="1" fill="none"/></symbol>
</svg>

<!-- Front card -->
<section class="card card--front" aria-label="Business card, front">
  <div class="card__band"></div>
  <div class="card__stripe"></div>

  <div class="brand" style="left:70px; top:60px;">
    <span class="brand__dot"></span>
    <span class="brand__name"><span class="line1">Brightwater</span><span class="line2">Meridale Wellness Clinic</span></span>
  </div>

  <div class="identity" style="left:70px; top:176px;">
    <p class="identity__name">Dr. Marcus T. Falk</p>
    <p class="identity__title">Chiropractic Physician</p>
    <p class="identity__address">5182 Orvalle Park Rd. Ste. B<br>Sarasota, FL 34871</p>
  </div>

  <div class="divider" style="left:300px; top:172px; height:104px;"></div>

  <ul class="contacts" style="left:314px; top:178px;">
    <li><svg><use href="#icon-phone"/></svg>941.555.0143</li>
    <li><svg><use href="#icon-fax"/></svg>941.555.0144</li>
    <li><svg style="fill:none;stroke:var(--green);stroke-width:1.4"><use href="#icon-mail"/></svg>wellpath7crew@mailnest.example</li>
    <li><svg><use href="#icon-web"/></svg>www.falkspinecare.example</li>
  </ul>
</section>

<!-- Back card -->
<section class="card card--back" aria-label="Business card, back">
  <div class="card__band"></div>
  <div class="card__stripe"></div>

  <div class="identity" style="left:282px; top:56px;">
    <p class="identity__name">Dr. Marcus T. Falk</p>
    <p class="identity__title">Chiropractic Physician</p>
    <p class="identity__address">5182 Orvalle Park Rd. Ste. B<br>Sarasota, FL 34871</p>
  </div>

  <div class="divider" style="left:266px; top:48px; height:262px;"></div>

  <div class="brand" style="left:56px; top:180px;">
    <span class="brand__dot" style="width:42px;height:42px;"></span>
    <span class="brand__name"><span class="line1" style="font-size:24px;">Brightwater</span><span class="line2" style="font-size:10.5px;">Meridale Wellness Clinic</span></span>
  </div>

  <ul class="contacts" style="left:282px; top:200px;">
    <li><svg><use href="#icon-phone"/></svg>941.555.0143</li>
    <li><svg><use href="#icon-fax"/></svg>941.555.0144</li>
    <li><svg style="fill:none;stroke:var(--green);stroke-width:1.4"><use href="#icon-mail"/></svg>wellpath7crew@mailnest.example</li>
    <li><svg><use href="#icon-web"/></svg>www.falkspinecare.example</li>
  </ul>
</section>

</body>
</html>
```